Boutique Film/TV Company needs Business Card Design

Please see our website for background on our company and look of our current logo: www.morlandpictures.ca

Pantone 314U is our main colour.

Target Market(s)

Network of peers, funders and broadcasters.

Industry/Entity Type

Business

Requirements
Must have
• We would like rounded corners and the height of the card to be shorter than traditional (maybe?!)

It's important that we have room for our office address, office number, cell number, email address, website, facebook and linked-in info (though not all of us have a linked-in account).

Would like the logo to keep the exclamation marks over the letters but the tag line/tag words of "film - television - interactive" can stay or go or... surprise me!

Nice to have
• Silky matte finish.

We are open to a change in the font of our logo/name.

```html
<!DOCTYPE html>
<html lang="en">
<head>
<meta charset="utf-8">
<title>Morland Business Card</title>
<link href="https://fonts.googleapis.com/css2?family=Maven+Pro:wght@400;500;700&display=swap" rel="stylesheet">
<style>
  :root {
    --teal: #01809f;
    --navy: #2b3b52;
    --white: #ffffff;
    --stage: #9c9c9c;
    --badge-top: #0a88b5;
    --badge-bottom: #1a5b86;
    --font: "Maven Pro", sans-serif;
  }
  html, body {
    margin: 0;
    width: 1200px;
    height: 1000px;
    overflow: hidden;
    background: var(--stage);
    font-family: var(--font);
  }
  .card {
    position: absolute;
    overflow: hidden;
    border-radius: 10px;
    background: var(--teal);
  }
  .card--front { left: 40px; top: 40px; width: 753px; height: 427px; }
  .card--back  { left: 384px; top: 517px; width: 754px; height: 428px; }
  .card__swoosh { position: absolute; inset: 0; width: 100%; height: 100%; }
  .brand-badge {
    position: absolute;
    width: 255px;
    height: 134px;
    border-radius: 3px;
    background: linear-gradient(180deg, var(--badge-top), var(--badge-bottom));
    color: var(--white);
    text-align: center;
    box-sizing: border-box;
    padding-top: 26px;
  }
  .card--front .brand-badge { left: 0; top: 150px; }
  .card--back .brand-badge { left: 262px; top: 158px; }
  .brand-badge__name {
    font-size: 50px;
    font-weight: 500;
    line-height: 56px;
    letter-spacing: 1px;
  }
  .brand-badge__tagline {
    font-size: 11.5px;
    font-weight: 700;
    margin-top: 8px;
  }
  .identity {
    position: absolute;
    right: 45px;
    top: 132px;
    text-align: right;
    color: var(--white);
  }
  .identity__name {
    font-size: 34px;
    font-weight: 400;
    letter-spacing: 3px;
    line-height: 36px;
  }
  .identity__surname { color: var(--navy); }
  .identity__title {
    font-size: 13px;
    font-style: italic;
    font-weight: 500;
    letter-spacing: 0.5px;
  }
  .contact {
    position: absolute;
    right: 40px;
    top: 216px;
    margin: 0;
    padding: 0;
    list-style: none;
    color: var(--white);
    font-size: 12px;
    font-weight: 500;
    letter-spacing: 0.6px;
  }
  .contact__item {
    display: flex;
    justify-content: flex-end;
    align-items: center;
    gap: 6px;
    text-align: right;
    line-height: 14px;
    margin-bottom: 9px;
  }
  .contact__item--email { font-size: 13px; }
  .contact__icon { width: 18px; height: 18px; flex: none; }
</style>
</head>
<body>

<section class="card card--front">
  <svg class="card__swoosh" viewBox="0 0 753 427" preserveAspectRatio="none" aria-hidden="true">
    <path d="M0,105 C180,250 380,380 753,362 L753,427 L0,427 Z" fill="var(--white)"/>
    <path d="M0,262 C160,350 400,430 753,366 L753,427 L0,427 Z" fill="var(--navy)"/>
  </svg>

  <div class="brand-badge">
    <div class="brand-badge__name">Morland</div>
    <div class="brand-badge__tagline">Films • Television • Interactive</div>
  </div>

  <header class="identity">
    <div class="identity__name">Elena<span class="identity__surname">Marsh</span></div>
    <div class="identity__title">Executive Manager</div>
  </header>

  <ul class="contact">
    <li class="contact__item">
      <span>140 Harbourview Lane, Suite 210<br>Toronto, Ontario M4K 2R7</span>
      <svg class="contact__icon" viewBox="0 0 18 18"><path d="M9 1a6 6 0 0 0-6 6c0 4 6 10 6 10s6-6 6-10a6 6 0 0 0-6-6z" fill="var(--navy)"/></svg>
    </li>
    <li class="contact__item contact__item--email">
      <span>elenamarsh@morland.com</span>
      <svg class="contact__icon" viewBox="0 0 18 18"><rect x="1.5" y="4" width="15" height="10" fill="none" stroke="var(--navy)" stroke-width="1.2"/><path d="M1.5 4l7.5 6 7.5-6M1.5 14l5.5-5M16.5 14l-5.5-5" fill="none" stroke="var(--navy)" stroke-width="1.2"/></svg>
    </li>
    <li class="contact__item">
      <span>416 555 0142</span>
      <svg class="contact__icon" viewBox="0 0 18 18"><rect x="5.5" y="2" width="7" height="14" rx="1" fill="none" stroke="var(--navy)" stroke-width="1.2"/><rect x="7" y="4" width="4" height="5" fill="var(--navy)"/></svg>
    </li>
    <li class="contact__item">
      <span>www.morlandpictures.ca</span>
      <svg class="contact__icon" viewBox="0 0 18 18"><g fill="none" stroke="var(--navy)" stroke-width="1.1"><circle cx="9" cy="9" r="7"/><ellipse cx="9" cy="9" rx="3" ry="7"/><path d="M2 9h14M3 5.5h12M3 12.5h12"/></g></svg>
    </li>
  </ul>
</section>

<section class="card card--back">
  <svg class="card__swoosh" viewBox="0 0 754 428" preserveAspectRatio="none" aria-hidden="true">
    <path d="M330,0 C540,30 690,130 754,262 L754,0 Z" fill="var(--white)"/>
    <path d="M415,0 C570,25 690,95 754,158 L754,0 Z" fill="var(--navy)"/>
  </svg>

  <div class="brand-badge">
    <div class="brand-badge__name">Morland</div>
    <div class="brand-badge__tagline">Films • Television • Interactive</div>
  </div>
</section>

</body>
</html>
```